Product flyer with pricing

We manufacture iconic and luxury vending trailers. for our first trailer we need a flyer created to give to prospective clients with base pricing. I am uploading an example along with graphic files.

```html
<!DOCTYPE html>
<html lang="en">
<head>
<meta charset="utf-8">
<title>The Meadow Barn Mini – Product Flyer</title>
<link href="https://fonts.googleapis.com/css2?family=Montserrat:wght@400;500;600;700;800&display=swap" rel="stylesheet">
<style>
  :root{
    --green:#5a9a3c;
    --green-dark:#4a8530;
    --orange:#f3a623;
    --ink:#333639;
    --panel:#ededed;
    --band:#e7e7e7;
    --header:#3f4245;
    --footer-dark:#3a3b3d;
    --white:#ffffff;
  }
  *{box-sizing:border-box;margin:0;padding:0}
  html,body{width:817px;height:1200px;overflow:hidden;background:#fff}
  body{font-family:"Montserrat",Arial,sans-serif;color:var(--ink)}
  .flyer{position:relative;width:817px;height:1200px;overflow:hidden;background:var(--white)}

  .hero{position:absolute;left:0;top:0;width:817px;height:260px;
    background:linear-gradient(180deg,#3b3f42 0%,#4c5155 55%,#3e4246 100%)}
  .grey-band{position:absolute;left:0;top:260px;width:817px;height:170px;background:var(--band)}

  .brand-tab{position:absolute;left:301px;top:0;width:215px;height:80px;background:var(--white);
    border-radius:0 0 14px 14px;display:flex;align-items:center;justify-content:center;gap:7px}
  .brand-dot{width:11px;height:11px;border-radius:50%;background:var(--green);flex:none}
  .brand-name{font-weight:700;font-size:14px;color:var(--green);letter-spacing:.3px;white-space:nowrap}

  .title{position:absolute;left:0;top:98px;width:817px;text-align:center;color:var(--white);
    font-weight:700;font-size:31px;letter-spacing:.5px;white-space:nowrap}
  .subtitle{position:absolute;left:208px;top:141px;width:402px;height:30px;background:var(--orange);
    border-radius:8px;color:var(--white);font-weight:700;font-size:19px;letter-spacing:.6px;
    display:flex;align-items:center;justify-content:center;white-space:nowrap}

  .gallery{position:absolute;top:210px;left:0;width:817px;height:158px}
  .thumb{position:absolute;top:0;width:152px;height:158px;border:2px solid var(--orange);
    background:linear-gradient(180deg,#b9cde0 0%,#e9ecef 45%,#f7f7f7 70%,#9ea2a6 100%)}

  .price{position:absolute;left:244px;top:390px;width:330px;height:60px;border-radius:14px;
    background:var(--green);padding:4px}
  .price span{display:flex;width:100%;height:100%;border:2px solid var(--white);border-radius:11px;
    align-items:center;justify-content:center;color:var(--white);font-weight:700;font-size:26px;letter-spacing:.6px;white-space:nowrap}

  .section-tab{position:absolute;left:42px;height:37px;background:var(--green);color:var(--white);
    font-weight:700;font-size:20px;letter-spacing:.6px;padding:0 19px;display:flex;align-items:center;
    border-radius:0 12px 0 0;z-index:2;white-space:nowrap}
  .panel{position:absolute;left:49px;width:720px;background:var(--panel);border-radius:0 18px 0 0}

  .ticks{list-style:none;font-size:15px;line-height:19px}
  .ticks li{position:relative;padding-left:23px;margin-bottom:10px}
  .ticks li::before{content:"";position:absolute;left:0;top:4px;width:12px;height:12px;border-radius:50%;
    background:var(--orange)}
  .ticks li::after{content:"";position:absolute;left:3.5px;top:6.5px;width:4px;height:6px;
    border:solid var(--white);border-width:0 1.6px 1.6px 0;transform:rotate(45deg)}

  .features{top:492px;height:210px}
  .features .col-a{position:absolute;left:12px;top:42px;width:390px}
  .features .col-b{position:absolute;left:442px;top:42px;width:270px}

  .options{position:absolute;left:61px;top:785px;width:700px;height:120px}
  .option{position:absolute;height:51px;display:flex}
  .option .label{background:var(--orange);color:var(--white);font-weight:600;font-size:12.5px;line-height:14px;
    display:flex;align-items:center;padding:0 8px;white-space:nowrap}
  .option .cost{background:#efefef;font-weight:600;font-size:26px;display:flex;flex-direction:column;
    justify-content:center;padding:0 8px;white-space:nowrap}
  .option .cost sup{font-size:13px;font-weight:600;vertical-align:top;margin-right:1px}
  .option .cost small{font-size:12.5px;font-weight:500;line-height:13px;margin-top:-2px}

  .uses{top:946px;height:154px}
  .uses .ticks{position:absolute;left:12px;top:42px;font-size:15px}
  .uses .ticks li{margin-bottom:7px}

  .footer{position:absolute;left:0;top:1130px;width:817px;height:70px}
  .footer svg{position:absolute;left:0;top:0}
  .phone{position:absolute;left:46px;top:1140px;display:flex;align-items:center;gap:8px;color:var(--white);
    font-weight:700;font-size:29px;white-space:nowrap}
  .contacts{position:absolute;right:40px;top:1148px;height:26px;display:flex;align-items:center;gap:16px}
  .contact{display:flex;align-items:center;gap:6px;font-size:14px;font-weight:500;white-space:nowrap}
  .divider{width:1px;height:24px;background:#cfcfcf}
</style>
</head>
<body>
<main class="flyer">
  <div class="hero" role="img" aria-label="Photo of the tiny vending house beside trees at dusk, darkened"></div>
  <div class="grey-band"></div>

  <div class="brand-tab"><span class="brand-dot"></span><span class="brand-name">LITTLE SUN BUILDS</span></div>

  <h1 class="title">The MEADOW BARN MINI</h1>
  <div class="subtitle">LUXURY, MOBILE VENDING HOUSE</div>

  <div class="gallery">
    <div class="thumb" style="left:49px" role="img" aria-label="Vending house side view with serving window open"></div>
    <div class="thumb" style="left:237px" role="img" aria-label="Vending house side view on tandem trailer"></div>
    <div class="thumb" style="left:426px" role="img" aria-label="Vending house rear corner view"></div>
    <div class="thumb" style="left:615px" role="img" aria-label="Vending house front gable with black door"></div>
  </div>

  <div class="price"><span>BASE PRICE: $45,000</span></div>

  <div class="section-tab" style="top:483px">BASE UNIT FEATURES</div>
  <section class="panel features">
    <ul class="ticks col-a">
      <li>Trailer features tandem wheels w/ brakes</li>
      <li>Steel frame construction for fire retardation safety and weight reduction.</li>
      <li>100% off grid with solar and lithium battery system allowing the trailer to be used in places not accessible by traditional trailers.</li>
    </ul>
    <ul class="ticks col-b">
      <li>80 gallon water supply tank</li>
      <li>100 gallon waste water tank</li>
      <li>Cupboards, cabinets &amp; four stainless steel sinks.</li>
      <li>60” Gas shock serving window</li>
    </ul>
  </section>

  <div class="section-tab" style="top:731px">AVAILABLE OPTIONS</div>
  <section class="options">
    <div class="option" style="left:0;top:0"><span class="label" style="width:108px">HVAC - Kelvo<br>Mini Split</span><span class="cost" style="width:100px"><span><sup>$</sup>1,800</span></span></div>
    <div class="option" style="left:228px;top:0"><span class="label" style="width:104px">Upper loft<br>storage area</span><span class="cost" style="width:110px"><span><sup>$</sup>1,200</span></span></div>
    <div class="option" style="left:468px;top:0"><span class="label" style="width:139px">Cooler / Glass<br>front Commercial<br>refrigerator</span><span class="cost" style="width:104px"><span><sup>$</sup>1,600</span></span></div>
    <div class="option" style="left:0;top:64px"><span class="label" style="width:101px">Signage and<br>graphics</span><span class="cost" style="width:218px"><span><sup>$</sup>2,000- <sup>$</sup>5,000</span><small>Depend on complexity</small></span></div>
    <div class="option" style="left:341px;top:64px"><span class="label" style="width:102px">Ice machine</span><span class="cost" style="width:103px"><span><sup>$</sup>1,100</span></span></div>
    <div class="option" style="left:568px;top:64px"><span class="label" style="width:139px;justify-content:center;text-align:center">Other custom<br>items available<br>on request.</span></div>
  </section>

  <div class="section-tab" style="top:936px">USE CASES</div>
  <section class="panel uses">
    <ul class="ticks">
      <li>Food: Lemonade, Coffee, pizza, cookies, doughnuts, barbecue and more!</li>
      <li>Retail: Clothing, watches, jewelry, flowers and more!</li>
      <li>Corporate: Product info, demonstration, information, brand awareness.</li>
      <li>Fundraisers: Girls/boy sports, non profits, etc.</li>
    </ul>
  </section>

  <footer class="footer">
    <svg width="817" height="70" viewBox="0 0 817 70" aria-hidden="true">
      <rect x="0" y="57" width="817" height="13" fill="var(--footer-dark)"/>
      <path d="M0 0 H300 C330 0 335 57 370 57 H0 Z" fill="var(--orange)"/>
      <path d="M0 0 H286 C314 0 320 57 352 57 H0 Z" fill="var(--green)"/>
    </svg>
  </footer>
  <div class="phone">
    <svg width="24" height="24" viewBox="0 0 24 24" aria-hidden="true"><path fill="#fff" d="M6.6 10.8a15.1 15.1 0 0 0 6.6 6.6l2.2-2.2c.3-.3.7-.4 1-.2 1.1.4 2.3.6 3.6.6.6 0 1 .4 1 1V20c0 .6-.4 1-1 1A17 17 0 0 1 3 4c0-.6.4-1 1-1h3.5c.6 0 1 .4 1 1 0 1.3.2 2.5.6 3.6.1.3 0 .7-.2 1z"/></svg>
    <span>0161 555 0198</span>
  </div>
  <div class="contacts">
    <div class="contact">
      <svg width="14" height="14" viewBox="0 0 14 14" aria-hidden="true"><circle cx="7" cy="7" r="6" fill="none" stroke="var(--orange)" stroke-width="1.4"/><ellipse cx="7" cy="7" rx="2.6" ry="6" fill="none" stroke="var(--orange)" stroke-width="1.2"/><path d="M1 7h12" stroke="var(--orange)" stroke-width="1.2"/></svg>
      <span>www.meadowbarn.com</span>
    </div>
    <div class="divider"></div>
    <div class="contact">
      <svg width="16" height="12" viewBox="0 0 16 12" aria-hidden="true"><rect x="0.7" y="0.7" width="14.6" height="10.6" fill="none" stroke="var(--orange)" stroke-width="1.4"/><path d="M1 1l7 6 7-6" fill="none" stroke="var(--orange)" stroke-width="1.4"/></svg>
      <span>info@meadowbarn.co.uk</span>
    </div>
  </div>
</main>
</body>
</html>
```